Lone Prairie Canvas & Sound Jubilee

Organization:
Lone Prairie Canvas and Sound Jubilee is a non-profit organization created by a group of anonymous donors to bring more fun, culture, and art to a small Texas town. Our mission is to promote art and music in Washington County.
The multi-day eclectic festival will feature three stages, a film, art vendors, live mural artists, and food trucks set up throughout historic downtown Brenham. The event is FREE to the public.
Goals:
We need an attractive poster to publicize the festival.
Details:
Lone Prairie Canvas and Sound Jubilee
Friday, October 14 – 16
Free admission (VIP tickets available)
Live music- 3 stages/10 bands
Film Screening
Art vendors and art walk
Live art murals
Food trucks
www.loneprairiecanvasandsoundjubilee.example
#loneprairiecanvasandsound
Requirements:
Please incorporate our festival logo attached.
Conclusion:
After selecting a poster design, we hope to continue to work with the artist to design other event materials including website splash page and rack cards using design elements from the poster.

```html
<!DOCTYPE html>
<html lang="en">
<head>
<meta charset="utf-8">
<title>Lone Prairie Canvas &amp; Sound Jubilee — Poster</title>
<link rel="stylesheet" href="https://fonts.googleapis.com/css2?family=Francois+One&family=Oswald:wght@400;600&display=swap">
<style>
  :root {
    --ink: #0c0c10;
    --ring: #1c1410;
    --paper: #ffffff;
    --sun: #ffd21a;
    --festival-red: #d8141a;
    --list-red: rgba(214, 28, 18, 0.88);
    --paint-red: #c8161c;
    --paint-yellow: #f2b418;
    --paint-blue: #1f3d8c;
    --paint-teal: #2f8c86;
    --night: #05070f;
    --glow-orange: #f06a12;
  }
  * { margin: 0; padding: 0; box-sizing: border-box; }
  html, body {
    width: 832px; height: 1200px; overflow: hidden;
    background: var(--ink);
  }
  .poster {
    position: relative;
    width: 832px; height: 1200px;
    overflow: hidden;
    background: var(--night);
    font-family: "Francois One", "Oswald", sans-serif;
  }
  .paint-swirl {
    position: absolute; left: 0; top: 0;
    width: 832px; height: 760px;
    background:
      radial-gradient(circle at 57% 28%, var(--ring) 0 24%, transparent 30%),
      conic-gradient(from 30deg at 57% 30%,
        var(--paint-red), var(--paint-yellow), var(--paint-blue), var(--paint-red),
        var(--paint-yellow), var(--paint-teal), var(--paint-red), var(--paint-yellow), var(--paint-red));
  }
  .music-photo {
    position: absolute; left: 0; top: 620px;
    width: 832px; height: 580px;
    background:
      radial-gradient(ellipse 40% 30% at 30% 40%, rgba(240,160,40,0.85), transparent 70%),
      radial-gradient(ellipse 45% 25% at 75% 45%, rgba(240,106,18,0.8), transparent 70%),
      radial-gradient(ellipse 50% 20% at 55% 75%, rgba(30,120,130,0.6), transparent 70%),
      linear-gradient(180deg, rgba(5,7,15,0) 0%, var(--night) 22%, #0a0d1c 100%);
  }
  .festival-badge {
    position: absolute; left: 274px; top: 136px;
    width: 400px; height: 400px;
  }
  .badge-title { font-family: "Francois One", sans-serif; font-size: 28px; fill: var(--sun); letter-spacing: 0.5px; }
  .badge-date { font-family: "Francois One", sans-serif; font-size: 33px; fill: var(--festival-red); letter-spacing: 1px; }
  .badge-name {
    position: absolute; left: 354px; top: 276px;
    width: 240px; height: 120px;
    display: flex; align-items: center; justify-content: center;
    text-align: center;
    color: var(--ink);
    font-size: 28px; line-height: 1.1;
    text-transform: uppercase;
  }
  .highlights {
    position: absolute; left: 388px; top: 580px;
    width: 444px; height: 222px;
    background: linear-gradient(90deg, var(--list-red), rgba(214,28,18,0.55));
    padding: 14px 0 0 20px;
    list-style: none;
  }
  .highlights li {
    display: flex; align-items: center; gap: 14px;
    color: var(--paper);
    font-size: 25px; line-height: 40px;
    text-transform: uppercase;
  }
  .highlights svg { flex: none; }
  .admission {
    position: absolute; left: 36px; top: 1110px;
    color: var(--sun);
    font-family: "Oswald", sans-serif;
  }
  .admission .free { font-weight: 600; font-size: 26px; line-height: 1.1; text-transform: uppercase; }
  .admission .vip { font-weight: 400; font-size: 19px; line-height: 1.2; }
  .contact {
    position: absolute; right: 26px; top: 1152px;
    display: flex; align-items: center; gap: 8px;
    color: var(--paper);
    font-family: "Oswald", sans-serif; font-size: 14px;
  }
  .contact .hashtag { margin-left: 20px; }
</style>
</head>
<body>
<main class="poster">
  <div class="paint-swirl" role="img" aria-label="Swirling thick brush strokes of red, yellow and blue oil paint"></div>
  <div class="music-photo" role="img" aria-label="Motion-blurred photo of a saxophone player and a guitarist's hands in warm stage light"></div>

  <svg class="festival-badge" viewBox="0 0 400 400" aria-hidden="true">
    <defs>
      <path id="arc-top" d="M 38 200 A 162 162 0 0 1 362 200"/>
      <path id="arc-bottom" d="M 18 200 A 182 182 0 0 0 382 200"/>
    </defs>
    <circle cx="200" cy="200" r="200" fill="var(--ring)"/>
    <circle cx="200" cy="200" r="142" fill="var(--paper)"/>
    <text class="badge-title"><textPath href="#arc-top" startOffset="50%" text-anchor="middle">LONE PRAIRIE CANVAS &amp; SOUND JUBILEE</textPath></text>
    <text class="badge-date"><textPath href="#arc-bottom" startOffset="50%" text-anchor="middle">FRIDAY - OCTOBER 14 - 16</textPath></text>
    <polygon points="22,186 25,195 34,195 27,200 30,209 22,204 14,209 17,200 10,195 19,195" fill="var(--paper)"/>
    <polygon points="378,186 381,195 390,195 383,200 386,209 378,204 370,209 373,200 366,195 375,195" fill="var(--paper)"/>
  </svg>
  <div class="badge-name">Lone Prairie Canvas &amp; Sound Jubilee</div>

  <ul class="highlights">
    <li><svg width="18" height="18" viewBox="0 0 18 18"><circle cx="9" cy="9" r="4" fill="var(--paper)"/><circle cx="9" cy="9" r="7.5" fill="none" stroke="var(--paper)" stroke-width="2" stroke-dasharray="2 2"/></svg>Live Music - 3 Stages/10 Bands</li>
    <li><svg width="18" height="18" viewBox="0 0 18 18"><circle cx="9" cy="9" r="4" fill="var(--paper)"/><circle cx="9" cy="9" r="7.5" fill="none" stroke="var(--paper)" stroke-width="2" stroke-dasharray="2 2"/></svg>Film Screening</li>
    <li><svg width="18" height="18" viewBox="0 0 18 18"><circle cx="9" cy="9" r="4" fill="var(--paper)"/><circle cx="9" cy="9" r="7.5" fill="none" stroke="var(--paper)" stroke-width="2" stroke-dasharray="2 2"/></svg>Live Art Murals</li>
    <li><svg width="18" height="18" viewBox="0 0 18 18"><circle cx="9" cy="9" r="4" fill="var(--paper)"/><circle cx="9" cy="9" r="7.5" fill="none" stroke="var(--paper)" stroke-width="2" stroke-dasharray="2 2"/></svg>Art Vendors and Art Walk</li>
    <li><svg width="18" height="18" viewBox="0 0 18 18"><circle cx="9" cy="9" r="4" fill="var(--paper)"/><circle cx="9" cy="9" r="7.5" fill="none" stroke="var(--paper)" stroke-width="2" stroke-dasharray="2 2"/></svg>Food Trucks</li>
  </ul>

  <div class="admission">
    <p class="free">Free Admission</p>
    <p class="vip">(VIP Tickets Available)</p>
  </div>

  <div class="contact">
    <svg width="16" height="16" viewBox="0 0 16 16" aria-hidden="true"><circle cx="8" cy="8" r="6.5" fill="none" stroke="var(--paper)" stroke-width="1.3"/><ellipse cx="8" cy="8" rx="2.8" ry="6.5" fill="none" stroke="var(--paper)" stroke-width="1.1"/><line x1="1.5" y1="8" x2="14.5" y2="8" stroke="var(--paper)" stroke-width="1.1"/></svg>
    <span class="url">www.loneprairiecanvasandsoundjubilee.example</span>
    <span class="hashtag">#loneprairiecanvasandsound</span>
  </div>
</main>
</body>
</html>
```